Internet service provider (ISP) flyer

Added Sep 8 - updated content language in brief below
Added Sep 8 - testimonials:

5 star rating on Voxelpeak
5 star rating on NorthlinkRate
"Unparalleled speeds, unlimited bandwith, amazing prices, immediate local customer service."
"Multiple Streamvue streams without issue"
"Fantastic for gaming. Very low ping..."
(End of testimonials)

--

We are looking for a 1/2 page double sided flyer to advertise our internet packages.

We provide Internet phone and TV services to residents living in condo buildings only.

Here is the content:

(Big heading must be on front)

Unlimited Fast Internet
Starting at $35 monthly

(Rest of content placement up to you)

(3 packages)

Fibre50 $35 monthly
50 Mbps download and upload speed
Unlimited Internet usage

Fibre250 $55 monthly
250 Mbps download and upload speed
Unlimited Internet usage

Fibre500 $75 monthly
500 Mbps download and upload speed
Unlimited Internet Usage

Gigabit Upgrade
LumaWire technicians built a gigabit fibre network in your building

No modems
Use your own wireless router or purchase from us.

No Contracts
Cancel any time, no notice required.

Local Support
Our team is located in Toronto and Ottawa

--

HD TELEVISION - add TV packages from $18 monthly

HOME PHONE - add Home Phone from $20 monthly

(our guarantee)

All LumaWire services include a risk free 30-day money back guarantee.

(contact information)

Your local sales rep:

Hank
(555) 482-3907
hank@lumawire-example.ca

Since 2009
Lumawire-example.ca
(555) 630-4418

Target Market(s)

Young professionals

Industry/Entity Type

Telecommunications

Font styles to use
Sans Serif
Other font styles liked:
• Roboto or Century Gothic

Colors
000000
f37122
acd136
757575

Requirements
Must have
• Front page that grabs attention
• Professional looking design
• Internet that looks fast
Nice to have
• Advanced fibre look and feel
• Dark / black background
• See attached images for look and feel samples
Should not have
• No cheesy corporate stock
• No images from our website

```html
<!DOCTYPE html>
<html lang="en">
<head>
<meta charset="utf-8">
<title>LumaWire Flyer</title>
<link href="https://fonts.googleapis.com/css2?family=Roboto:wght@300;400;500;700;900&display=swap" rel="stylesheet">
<style>
:root{
  --orange:#f05a22;
  --orange-soft:#f37122;
  --ink:#111111;
  --dark:#2b2a2a;
  --grey:#757575;
  --stage:#5f5c5c;
  --paper:#ffffff;
  --star:#f6c21c;
}
*{box-sizing:border-box;margin:0;padding:0}
html,body{width:1200px;height:1200px;overflow:hidden}
body{background:var(--stage);font-family:'Roboto',Arial,sans-serif;position:relative;color:var(--ink)}
.page{position:absolute;top:245px;width:504px;height:715px;background:var(--paper);overflow:hidden;box-shadow:0 6px 14px rgba(0,0,0,.35)}
.page--front{left:80px}
.page--back{left:630px}
.abs{position:absolute}

/* front */
.brand{left:26px;top:30px;font-size:38px;font-weight:500;color:var(--orange);letter-spacing:-.5px}
.brand-rule{left:0;top:88px;width:504px;height:6px;background:var(--orange)}
.hero-photo{left:0;top:94px;width:504px;height:333px;background:linear-gradient(120deg,#c9b79a 0%,#9aa59a 35%,#6f7d8f 65%,#d8d4cc 100%)}
.offer-shadow{left:44px;top:487px;width:422px;height:10px;background:#d9d9d9}
.offer{left:36px;top:413px;width:430px;height:80px;background:var(--orange);text-align:center;padding-top:6px}
.offer-title{font-size:35px;font-weight:700;color:var(--paper);line-height:40px;letter-spacing:-.3px}
.offer-title .dark{color:var(--ink)}
.offer-sub{font-size:25px;font-weight:400;color:var(--ink);line-height:28px;letter-spacing:.5px}
.offer-sub .light{color:var(--paper);font-weight:500}
.packages-title{left:0;top:518px;width:504px;text-align:center;font-size:24px;font-weight:700;color:var(--ink)}
.packages-title span{color:var(--orange);font-size:20px;font-weight:500}
.package{top:565px;width:160px}
.package-name{font-size:16px;font-weight:500;line-height:20px}
.package-price{display:inline-block;margin-top:2px;background:var(--orange);color:var(--paper);font-size:16px;font-weight:500;padding:1px 5px;width:108px;line-height:22px}
.package-speed{margin-top:4px;font-size:12px;line-height:15px;color:var(--ink)}
.package-speed b{font-weight:700}
.package-usage{font-size:12px;font-weight:700;color:var(--orange);line-height:15px}
.front-footer{left:0;top:686px;width:504px;height:29px;background:var(--ink);color:var(--paper);text-align:center;font-size:14px;line-height:29px}
.front-footer span{color:var(--orange)}

/* back */
.slogan{left:0;top:8px;width:504px;text-align:center;font-size:25px;font-weight:700;font-variant:small-caps;letter-spacing:.3px;color:var(--ink)}
.slogan span{color:var(--orange)}
.dark-panel{left:0;top:142px;width:504px;height:432px;background:var(--dark)}
.family-photo{left:83px;top:43px;width:337px;height:142px;border:3px solid var(--orange);background:linear-gradient(110deg,#e9e6e2 0%,#b5aca6 40%,#8a8f9a 70%,#d8d3cf 100%)}
.features-tab{left:0;top:209px;width:190px;height:30px;background:var(--orange);clip-path:polygon(0 0,100% 0,92% 100%,0 100%);font-size:20px;color:var(--paper);padding-left:30px;line-height:30px}
.features-tab b{font-weight:500;color:var(--ink)}
.feature{width:210px;color:var(--paper)}
.feature svg{position:absolute;left:0;top:4px}
.feature-title{padding-left:22px;font-size:17px;font-weight:500;line-height:20px}
.feature-text{padding-left:22px;margin-top:3px;font-size:11px;line-height:15px;color:#e4e4e4}
.addon{left:50px;width:420px;font-size:14px;color:var(--paper);line-height:18px;padding-left:30px}
.addon svg{position:absolute;left:0;top:1px}
.addon b{color:var(--orange);font-weight:500}
.quotes{left:52px;top:461px;width:386px;height:89px;border:3px solid var(--orange);border-top:none;border-bottom:none}
.quotes::before,.quotes::after{content:"";position:absolute;left:0;right:0;height:3px;background:var(--orange);clip-path:polygon(0 0,4% 0,4% 100%,0 100%,96% 100%,96% 0,100% 0,100% 100%,0 100%)}
.quotes::before{top:0;clip-path:polygon(0 0,4% 0,4% 100%,0 100%)}
.quotes::after{bottom:0;clip-path:polygon(96% 0,100% 0,100% 100%,96% 100%)}
.quote{left:12px;font-size:13px;color:var(--paper);line-height:16px}
.quote q{quotes:"\201C" "\201D"}
.quote q::before,.quote q::after{color:var(--orange)}
.review{top:586px;font-size:16px;color:var(--ink)}
.review sup{color:var(--star);font-size:11px;letter-spacing:1px}
.guarantee-title{left:20px;top:636px;font-size:15px;font-weight:700;color:var(--orange);text-decoration:underline}
.guarantee-text{left:20px;top:656px;width:222px;font-size:12px;font-weight:700;line-height:15px;color:var(--ink)}
.divider{left:250px;top:638px;width:2px;height:52px;background:var(--orange)}
.contact-title{left:266px;top:630px;font-size:15px;font-weight:500;color:var(--orange)}
.contact-note{left:266px;top:648px;font-size:9px;color:var(--ink)}
.contact-col{top:661px;font-size:9.5px;line-height:15px;color:var(--ink)}
.contact-col .tel{color:var(--orange)}
.back-rule{left:0;top:705px;width:504px;height:10px;background:var(--orange)}
</style>
</head>
<body>

<section class="page page--front">
  <div class="abs brand">LumaWire</div>
  <div class="abs brand-rule"></div>
  <div class="abs hero-photo" role="img" aria-label="Photo of young professionals using phones and a laptop outdoors"></div>
  <div class="abs offer-shadow"></div>
  <div class="abs offer">
    <h1 class="offer-title">Unlimited <span class="dark">Fast Internet</span></h1>
    <p class="offer-sub">STARTING AT <span class="light">$35</span> MONTHLY</p>
  </div>
  <h2 class="abs packages-title">3 Internet <span>PACKAGES :</span></h2>

  <div class="abs package" style="left:20px">
    <div class="package-name">Fibre 50</div>
    <div class="package-price">$35 monthly</div>
    <p class="package-speed"><b>50 Mbps</b><br>download and<br>upload speed</p>
    <p class="package-usage">Unlimited Internet usage</p>
  </div>
  <div class="abs package" style="left:179px">
    <div class="package-name">Fibre 250</div>
    <div class="package-price">$55 monthly</div>
    <p class="package-speed"><b>250 Mbps</b><br>download and<br>upload speed</p>
    <p class="package-usage">Unlimited Internet usage</p>
  </div>
  <div class="abs package" style="left:340px">
    <div class="package-name">Fibre 500</div>
    <div class="package-price">$75 monthly</div>
    <p class="package-speed"><b>500 Mbps</b><br>download and<br>upload speed</p>
    <p class="package-usage">Unlimited Internet usage</p>
  </div>

  <div class="abs front-footer">www.<span>lumawire-example</span>.ca</div>
</section>

<section class="page page--back">
  <h2 class="abs slogan">Better technology.<span>Faster Speeds.</span></h2>
  <div class="abs dark-panel"></div>
  <div class="abs family-photo" role="img" aria-label="Photo of a family relaxing on a sofa with laptops"></div>
  <div class="abs features-tab"><b>Our</b> Features</div>

  <div class="abs feature" style="left:16px;top:258px">
    <svg width="14" height="14" viewBox="0 0 14 14"><circle cx="7" cy="7" r="5" fill="none" stroke="#f05a22" stroke-width="3" stroke-dasharray="3 1.5"/><circle cx="7" cy="7" r="2" fill="#f05a22"/></svg>
    <div class="feature-title">Gigabit Upgrade</div>
    <p class="feature-text">We upgrade your condo building<br>with gigabit fibre technology</p>
  </div>
  <div class="abs feature" style="left:235px;top:258px">
    <svg width="14" height="14" viewBox="0 0 14 14"><circle cx="7" cy="7" r="5" fill="none" stroke="#f05a22" stroke-width="3" stroke-dasharray="3 1.5"/><circle cx="7" cy="7" r="2" fill="#f05a22"/></svg>
    <div class="feature-title">No Contracts</div>
    <p class="feature-text">Cancel anytime, no notice required.</p>
  </div>
  <div class="abs feature" style="left:16px;top:330px">
    <svg width="14" height="14" viewBox="0 0 14 14"><circle cx="7" cy="7" r="5" fill="none" stroke="#f05a22" stroke-width="3" stroke-dasharray="3 1.5"/><circle cx="7" cy="7" r="2" fill="#f05a22"/></svg>
    <div class="feature-title">No modems</div>
    <p class="feature-text">Use your own wireless router or<br>purchase from us.</p>
  </div>
  <div class="abs feature" style="left:235px;top:330px;width:260px">
    <svg width="14" height="14" viewBox="0 0 14 14"><circle cx="7" cy="7" r="5" fill="none" stroke="#f05a22" stroke-width="3" stroke-dasharray="3 1.5"/><circle cx="7" cy="7" r="2" fill="#f05a22"/></svg>
    <div class="feature-title">Local Support</div>
    <p class="feature-text">Our offices are located in North America.</p>
  </div>

  <p class="abs addon" style="top:398px">
    <svg width="20" height="16" viewBox="0 0 20 16"><rect x="1" y="1" width="18" height="11" fill="none" stroke="#fff" stroke-width="1.5"/><path d="M6 15h8M10 12v3" stroke="#fff" stroke-width="1.5"/></svg>
    <b>HD TELEVISION</b> - add TV packages from <b>$18</b> monthly
  </p>
  <p class="abs addon" style="top:420px">
    <svg width="20" height="16" viewBox="0 0 20 16"><rect x="3" y="1" width="14" height="14" rx="1.5" fill="none" stroke="#fff" stroke-width="1.5"/><path d="M6 4h8M6 8h2M9 8h2M12 8h2M6 11h2M9 11h2M12 11h2" stroke="#fff" stroke-width="1.3"/></svg>
    <b>HOME PHONE</b> - add Home Phone from <b>$20</b> monthly
  </p>

  <div class="abs quotes">
    <p class="abs quote" style="top:10px"><q>Unparalleled speeds, unlimited bandwith, amazing prices,<br>immediate local customer service.</q></p>
    <p class="abs quote" style="top:44px"><q>Multiple Streamvue streams without issue</q></p>
    <p class="abs quote" style="top:64px"><q>Fantastic for gaming. Very low ping...</q></p>
  </div>

  <p class="abs review" style="left:24px">Voxelpeak<sup>★★★★★</sup></p>
  <p class="abs review" style="left:294px">NorthlinkRate<sup>★★★★★</sup></p>

  <h3 class="abs guarantee-title">OUR GUARANTEE</h3>
  <p class="abs guarantee-text">All LumaWire services include a risk free 30-day money back guarantee.</p>
  <div class="abs divider"></div>
  <h3 class="abs contact-title">Contact Information</h3>
  <p class="abs contact-note">Your local sales rep:</p>
  <p class="abs contact-col" style="left:266px">Hank<br><span class="tel">(555) 482-3907</span><br>hank@lumawire-example.ca</p>
  <p class="abs contact-col" style="left:396px;top:648px">Since 2009<br>Lumawire-example.ca<br><span class="tel">(555) 630-4418</span></p>
  <div class="abs back-rule"></div>
</section>

</body>
</html>
```